Design Creative Banner or Gif Ads. 3 Designs To Be Selected

Come up with some creative banner ads for stonewell.co.nz

*At least 3 different winning banners will be chosen*

Please provide banner ads / gif ads in common google ads / website banner formats.

They can be gif or static but must stand out while still maintaining clear clean text and visuals, with a premium professional feel (please avoid clip art or anything that gives a cheap message).

Please keep in mind that these will likely be small ads so text needs to be large and if there's there a lot of text then use multiple frames/ pages as submit as a gif.

Style
Minimal & clean lines
Architectural or realistic images
Avoid cartoon styles, clipart, or anything that looks cheap

Font
Nexa or Montserrat or similar

Tone
Premium, serious, trustworthy — fits new builds

Colours
Option 1: Deep Navy (trust & quality) & lighter blues and warm grey
Option 2: Open to bright colours to help the ads stand out, such as (but not limited to) bright pink with black, yellow, fluorescent green, provided the messaging is still done professionally.
Our logo is attached (Stone Well Logo)

Display Sizes
Ad specs for file sizes should be file formats like JPEG, GIF, and PNG, with animations limited to a max of 30 seconds or less.
We will need several different ad sizes provided for each of the 3 selected winning designs.

• Medium Rectangle: 300 × 250 pixels
• Leaderboard: 728 × 90 pixels
• Desktop Banner ad image: (640x360 pixels)
• Desktop Banner ad image 2: (300x600 pixels)
• Possibly one or two other sizes

Flexibility to be creative
The ad text, words, upper/lower case, layout, colour, theme, and images can be adjusted to how you think it will look best. The follow example ads are just examples of what we are after but we are keen to see what you can create.

Recommendations at this point:
1. Avoid text heavy
2. Looking for more Gif ads
3. Imaging: if possible use real stock photo's rather than AI

Themes:

1
Building Soon? Start Here
Free Build Planning Pack:
✓ Build Cost Calculator
✓ Hidden Cost Checklist
✓ Builder Comparison Guide
Build With Confidence
Download Free

2
Before You Choose A Builder
Compare Price, Scope, Risk & Value
Avoid Costly Mistakes
Choose The Right Builder With Confidence
Download The Free Guide

3
Planning A New Build?
Avoid These Common Mistakes:
✗ Hidden Exclusions
✗ Missing Scope
✗ Unrealistic Allowances
✗ Budget Blowouts
Download The Free Guide

4
Before You Buy Land
Know what it could cost to build.
Avoid Costly Building Mistakes
Download Our Free Guides

5
Know Your Build Budget?
• Free Build Cost Calculator
• Hidden Cost Checklist
• Build Planning Tools
Calculate Costs (Download)

Target Market(s)

Landowners looking to build

Industry/Entity Type

Building

Font styles to use
Other font styles liked:
• Nexa or Montserrat or similar

Requirements
Should not have
• Avoid cartoon styles, clipart, or anything that looks cheap

```html
<!DOCTYPE html>
<html lang="en">
<head>
<meta charset="utf-8">
<title>Stone Well – Free Build Planning Pack</title>
<link rel="stylesheet" href="https://fonts.googleapis.com/css2?family=Montserrat:wght@300;400;500;600;700&display=swap">
<style>
  :root {
    --navy: #1f2a3a;
    --navy-text: #1c2737;
    --sky: #35a7d8;
    --band-blue: #1f74c8;
    --white: #ffffff;
    --suit-dark: #181b20;
    --facade-grey: #6f7478;
    --facade-light: #9a9d9c;
  }
  html, body {
    margin: 0;
    padding: 0;
    width: 1200px;
    height: 1001px;
    overflow: hidden;
    background: var(--white);
  }
  .banner {
    position: relative;
    width: 1200px;
    height: 1001px;
    overflow: hidden;
    font-family: "Montserrat", sans-serif;
    background: var(--white);
  }
  .banner-shapes {
    position: absolute;
    inset: 0;
  }
  .headline {
    position: absolute;
    left: 82px;
    top: 88px;
    margin: 0;
    font-weight: 600;
    font-size: 71px;
    line-height: 88px;
    letter-spacing: -0.6px;
    color: var(--white);
  }
  .headline .accent {
    color: var(--sky);
    display: block;
  }
  .subhead {
    position: absolute;
    left: 85px;
    top: 366px;
    margin: 0;
    font-weight: 600;
    font-size: 38px;
    letter-spacing: -0.3px;
    color: var(--white);
  }
  .divider {
    position: absolute;
    left: 88px;
    top: 448px;
    width: 535px;
    height: 2px;
    background: var(--sky);
  }
  .pack-title {
    position: absolute;
    left: 85px;
    top: 474px;
    margin: 0;
    font-weight: 600;
    font-size: 40px;
    letter-spacing: -0.3px;
    color: var(--white);
  }
  .pack-list {
    position: absolute;
    left: 84px;
    top: 557px;
    margin: 0;
    padding: 0;
    list-style: none;
  }
  .pack-list li {
    display: flex;
    align-items: center;
    height: 57px;
    font-weight: 400;
    font-size: 35px;
    color: var(--white);
  }
  .pack-list svg {
    width: 41px;
    height: 41px;
    margin-right: 15px;
    flex: none;
  }
  .download-button {
    position: absolute;
    left: 73px;
    top: 772px;
    width: 492px;
    height: 95px;
    border-radius: 5px;
    background: var(--sky);
    color: var(--white);
    text-decoration: none;
    display: flex;
    align-items: center;
  }
  .download-button svg {
    width: 52px;
    height: 56px;
    margin-left: 30px;
    margin-right: 64px;
    flex: none;
  }
  .download-button {
    gap: 0;
  }
  .download-label {
    display: flex;
    flex-direction: column;
    margin-left: -46px;
  }
  .download-main {
    font-weight: 700;
    font-size: 36px;
    letter-spacing: 2.5px;
    line-height: 40px;
  }
  .download-sub {
    font-weight: 500;
    font-size: 18px;
    letter-spacing: 1.6px;
    line-height: 26px;
  }
  .tagline {
    position: absolute;
    right: 83px;
    top: 736px;
    margin: 0;
    text-align: right;
    font-weight: 600;
    font-size: 34px;
    line-height: 46px;
    letter-spacing: -0.3px;
    color: var(--navy-text);
  }
  .brand {
    position: absolute;
    left: 642px;
    top: 852px;
    display: flex;
    align-items: center;
  }
  .brand-square {
    width: 66px;
    height: 66px;
    background: var(--navy);
    margin-right: 34px;
  }
  .brand-name {
    font-weight: 600;
    font-size: 64px;
    color: var(--navy-text);
    letter-spacing: -0.8px;
  }
</style>
</head>
<body>
<main class="banner">
  <svg class="banner-shapes" width="1200" height="1001" viewBox="0 0 1200 1001">
    <defs>
      <linearGradient id="photo-tone" x1="0" y1="0.3" x2="1" y2="0.1">
        <stop offset="0" stop-color="#2a2f36"/>
        <stop offset="0.35" stop-color="var(--suit-dark)"/>
        <stop offset="0.62" stop-color="#2c3034"/>
        <stop offset="0.82" stop-color="var(--facade-grey)"/>
        <stop offset="1" stop-color="var(--facade-light)"/>
      </linearGradient>
    </defs>
    <rect class="navy-field" x="0" y="0" width="1200" height="862" fill="var(--navy)"/>
    <polygon class="photo-area" role="img" aria-label="Photo of a smiling businessman in a dark suit with arms crossed, standing in front of a modern apartment building" points="855,0 1200,0 1200,617 623,716" fill="url(#photo-tone)"/>
    <polygon class="accent-band" points="0,824 1200,612 1200,624 0,862" fill="var(--band-blue)"/>
    <polygon class="white-field" points="0,862 1200,624 1200,1001 0,1001" fill="var(--white)"/>
  </svg>

  <h1 class="headline">Bought Land?<span class="accent">Avoid Costly</span><span class="accent">Build Mistakes</span></h1>
  <p class="subhead">Discover The Hidden Costs</p>
  <div class="divider"></div>

  <h2 class="pack-title">Free Build Planning Pack</h2>
  <ul class="pack-list">
    <li><svg viewBox="0 0 40 40" aria-hidden="true"><circle cx="20" cy="20" r="20" fill="var(--sky)"/><path d="M11.5 20.5l6 6 11-12" fill="none" stroke="#fff" stroke-width="3.5" stroke-linecap="round" stroke-linejoin="round"/></svg>Build Cost Calculator</li>
    <li><svg viewBox="0 0 40 40" aria-hidden="true"><circle cx="20" cy="20" r="20" fill="var(--sky)"/><path d="M11.5 20.5l6 6 11-12" fill="none" stroke="#fff" stroke-width="3.5" stroke-linecap="round" stroke-linejoin="round"/></svg>Build Journey Roadmap</li>
    <li><svg viewBox="0 0 40 40" aria-hidden="true"><circle cx="20" cy="20" r="20" fill="var(--sky)"/><path d="M11.5 20.5l6 6 11-12" fill="none" stroke="#fff" stroke-width="3.5" stroke-linecap="round" stroke-linejoin="round"/></svg>Hidden Cost Checklist</li>
  </ul>

  <a class="download-button" href="#">
    <svg viewBox="0 0 52 56" aria-hidden="true">
      <path d="M26 2v36M13 26l13 13 13-13" fill="none" stroke="#fff" stroke-width="3" stroke-linecap="round" stroke-linejoin="round"/>
      <path d="M2 44v9h48v-9" fill="none" stroke="#fff" stroke-width="3" stroke-linecap="round" stroke-linejoin="round"/>
    </svg>
    <span class="download-label">
      <span class="download-main">DOWNLOAD</span>
      <span class="download-sub">(FREE BUILD PLANNING PACK)</span>
    </span>
  </a>

  <p class="tagline">Choose The Right Builder<br>With Clarity &amp; Confidence.</p>

  <div class="brand">
    <div class="brand-square"></div>
    <span class="brand-name">Stone Well</span>
  </div>
</main>
</body>
</html>
```